Alloy wheel repair business needs a website

Install logo previously purchased from vantoquill, toolbar with dropdowns. services, gallery, clients , contact ect
Maybe mission statment

Target Market(s)

vehicle owners, auto dealers,insurance companies,

Industry/Entity Type

Alloy Wheel Repair

Coding

Coded - Design and coding required

Number of Pages Required

4 page

Font styles to use
Sans Serif

Colors
0054AA
0677BA
7BADD7
CADEEF
E8F1F8

```html
<!DOCTYPE html>
<html lang="en">
<head>
<meta charset="utf-8">
<title>Rimhaven Wheelcraft – Style Board and Home Page</title>
<link href="https://fonts.googleapis.com/css2?family=Barlow:wght@400;500;600;700&display=swap" rel="stylesheet">
<style>
:root{
  --ink:#1e1e1d;
  --blue:#468cc9;
  --mist:#f1f2f3;
  --board:#e0e0e0;
  --black:#0b0b0b;
  --muted:#7a7a7a;
  --white:#ffffff;
}
*{box-sizing:border-box;margin:0;padding:0}
html,body{width:1200px;height:2801px;overflow:hidden}
body{background:var(--board);font-family:'Barlow',sans-serif;color:var(--ink);position:relative}
.abs{position:absolute}

/* style board header */
.board-brand{left:205px;top:128px;font-size:26px;font-weight:700;color:var(--blue);letter-spacing:1px;line-height:1.05}
.board-brand span{display:block;font-size:13px;color:var(--ink);letter-spacing:4px}
.board-label{font-size:25px;font-weight:500;color:#333}
.board-font{left:597px;top:148px;font-size:16px;color:#555}
.swatch{width:41px;height:41px;border-radius:50%;top:137px}
.swatch-label{top:187px;font-size:9px;color:#555;width:60px;text-align:center}

/* site */
.site{left:226px;top:277px;width:783px;background:var(--white)}
.section{position:relative;width:783px;overflow:hidden}

.hero{height:496px;background:radial-gradient(ellipse at 72% 35%,#6d6f72 0%,#2e2f31 32%,#161617 65%),var(--ink)}
.brand{font-weight:700;color:var(--white);font-size:15px;letter-spacing:1px;line-height:1}
.brand small{display:block;font-size:7px;letter-spacing:3px;font-weight:600}
.nav{top:19px;left:309px;display:flex;gap:10px;font-size:7.5px;color:var(--white)}
.nav i{font-style:normal;color:#888}
.search{left:652px;top:16px}
.hero-kicker{left:100px;top:124px;font-size:14.5px;color:var(--white)}
.hero-title{left:100px;top:140px;font-size:43px;font-weight:700;color:var(--white);letter-spacing:-.5px}
.hero-sub{left:101px;top:195px;font-size:9.5px;color:#c9c9c9;letter-spacing:.3px}
.btn-outline{left:103px;top:230px;width:93px;height:31px;border:1px solid var(--blue);color:var(--white);font-size:7.5px;font-weight:600;display:flex;align-items:center;justify-content:center;gap:5px}
.service-strip{left:0;top:345px;width:783px;height:151px;display:flex;background:rgba(10,10,10,.55);border-top:1px solid #333}
.service{flex:1;position:relative;border-right:1px solid #333}
.service:last-child{border-right:0}
.service-art{position:absolute;left:14px;top:22px;width:108px;height:108px;border-radius:50%;background:radial-gradient(circle,#c9cbcd 0%,#66686b 45%,#262627 75%)}
.service h3{position:absolute;left:139px;top:27px;font-size:13px;font-weight:600;color:var(--white);line-height:1.2}
.service p{position:absolute;left:139px;top:68px;width:100px;font-size:7px;line-height:1.7;color:#bdbdbd}
.service a{position:absolute;left:139px;top:115px;font-size:7.5px;color:var(--blue);text-decoration:none}

.mission{height:336px;background:var(--mist)}
.sec-title{width:100%;text-align:center;font-size:22px;font-weight:600}
.sec-text{left:241px;width:302px;text-align:center;font-size:7.6px;line-height:1.75;color:#555}
.feature{width:90px;text-align:center;font-size:7.8px;line-height:1.35;color:#333}
.feature svg{display:block;margin:0 auto 3px}
.car-art{left:224px;top:160px;width:236px;height:108px;border-radius:40% 45% 10% 10%;background:linear-gradient(180deg,#f7f7f7 0%,#dcdcdc 60%,#2a2a2a 100%)}
.wheels-art{left:487px;top:176px;width:102px;height:100px;border-radius:50%;background:radial-gradient(circle,#d5d5d5 0%,#8a8a8a 40%,#1d1d1d 70%)}

.video{height:183px;background:radial-gradient(ellipse at 72% 70%,#1f4fb0 0%,transparent 25%),linear-gradient(120deg,#161616 0%,#4a4a4a 40%,#2b2b2b 70%,#101010 100%)}
.play{left:358px;top:58px;width:66px;height:66px;border-radius:50%;background:rgba(255,255,255,.18);border:1px solid rgba(255,255,255,.4)}

.what{height:317px;background:var(--white)}
.offer{width:130px;text-align:center}
.offer h4{font-size:9px;font-weight:600;margin-top:6px}
.offer p{font-size:7px;line-height:1.6;color:#888;margin-top:3px}

.gallery{height:401px;background:linear-gradient(160deg,#1b1b1b 0%,#0a0a0a 70%)}
.gal-title{left:101px;top:56px;font-size:24px;font-weight:600;color:var(--white);line-height:1.1}
.circle-btn{width:34px;height:34px;border-radius:50%;top:130px;display:flex;align-items:center;justify-content:center}
.view-all{left:101px;top:185px;font-size:7.5px;font-weight:600;color:var(--white)}
.shot{width:183px;height:140px;background:radial-gradient(ellipse at 40% 45%,#e4e4e4 0%,#9c9c9c 45%,#2f2f2f 90%)}

.reviews{height:356px;background:linear-gradient(90deg,#fff 85%,#eceded 100%)}
.card{width:183px;height:156px;top:106px;background:var(--mist);padding:0 13px}
.card-head{height:41px;border-bottom:1px solid #dcdcdc;display:flex;align-items:center;gap:8px;position:relative}
.avatar{width:17px;height:17px;border-radius:50%;background:#b8b0a8}
.who{font-size:7px;line-height:1.3}
.who small{display:block;font-size:5.5px;color:#999}
.source{position:absolute;right:0;top:16px;width:8px;height:8px;border-radius:50%;border:1px solid var(--blue)}
.stars{margin-top:10px;color:#f2b31b;font-size:8px;letter-spacing:1px}
.card p{font-size:6.8px;line-height:1.8;color:#666;margin-top:4px}
.dots{left:369px;top:290px;display:flex;gap:4px}
.dots b{width:6px;height:6px;border-radius:50%;border:1px solid var(--blue)}
.dots b.on{background:var(--blue)}

.footer{height:324px;background:radial-gradient(ellipse at 25% 20%,#262626 0%,#050505 55%)}
.social{top:94px;width:15px;height:15px;border-radius:50%;background:var(--blue)}
.f-head{font-size:8.5px;font-weight:600;color:var(--white)}
.f-list{font-size:6.5px;color:#8a8a8a;line-height:14px}
.email{left:474px;top:94px;width:133px;border-bottom:1px solid #444;padding-bottom:6px;font-size:6px;color:#888}
.subscribe{left:607px;top:84px;width:74px;height:24px;background:var(--blue);color:var(--white);font-size:6.5px;font-weight:600;display:flex;align-items:center;justify-content:center}
.f-rule{left:0;top:289px;width:783px;height:1px;background:#222}
.legal{top:302px;font-size:5.5px;color:#aaa;font-weight:600}
</style>
</head>
<body>

<!-- style board header -->
<div class="abs board-brand">RIMHAVEN<span>WHEELCRAFT</span></div>
<div class="abs board-label" style="left:596px;top:100px">Fonts:</div>
<div class="abs board-font">Barlow</div>
<div class="abs board-label" style="left:889px;top:100px">Colors:</div>
<div class="abs swatch" style="left:889px;background:var(--ink)"></div>
<div class="abs swatch" style="left:941px;background:var(--blue)"></div>
<div class="abs swatch" style="left:992px;background:var(--mist)"></div>
<div class="abs swatch-label" style="left:880px">#1e1e1d</div>
<div class="abs swatch-label" style="left:932px">#468cc9</div>
<div class="abs swatch-label" style="left:983px">#f1f2f3</div>

<main class="abs site">

  <section class="section hero">
    <div class="abs" role="img" aria-label="Close-up photo of a silver alloy wheel on a tyre" style="left:430px;top:60px;width:220px;height:300px;border-radius:50%;background:radial-gradient(ellipse,#c8cacc 0%,#7b7d80 40%,transparent 70%);opacity:.55"></div>
    <div class="abs brand" style="left:104px;top:12px">RIMHAVEN<small>WHEELCRAFT</small></div>
    <nav class="abs nav"><span>Home</span><i>/</i><span>Services</span><i>/</i><span>Gallery</span><i>/</i><span>Clients</span><i>/</i><span>Contact</span></nav>
    <svg class="abs search" width="12" height="12" viewBox="0 0 12 12"><circle cx="5" cy="5" r="3.8" fill="none" stroke="#fff" stroke-width="1"/><line x1="8" y1="8" x2="11" y2="11" stroke="#fff" stroke-width="1"/></svg>
    <div class="abs hero-kicker">Unlocking the Excellence in</div>
    <h1 class="abs hero-title">AlloyWheel</h1>
    <div class="abs hero-sub">- Your Trusted Source for Wheel Refurbishment</div>
    <div class="abs btn-outline">How it Works <svg width="5" height="7" viewBox="0 0 5 7"><path d="M1 1l2.5 2.5L1 6" stroke="#fff" fill="none"/></svg></div>

    <div class="abs service-strip">
      <div class="service">
        <div class="service-art" role="img" aria-label="Illustration of a tyre with alloy wheel"></div>
        <h3>Wheel Repair<br>Services</h3>
        <p>Restore &amp; rejuvenate any damaged wheels with great precision and care</p>
        <a>Request a Quote &nbsp;›</a>
      </div>
      <div class="service">
        <div class="service-art" role="img" aria-label="Illustration of a wheel with wrench and tools"></div>
        <h3>Wheel Replace<br>Services</h3>
        <p>Get back on the road swiftly and securely with our efficient wheel replacement service</p>
        <a>Request a Quote &nbsp;›</a>
      </div>
      <div class="service">
        <div class="service-art" role="img" aria-label="Illustration of a paint spray gun" style="background:radial-gradient(circle,#7fb0de 0%,#5a5c60 45%,#262627 75%)"></div>
        <h3>Custom Wheel<br>Coloring</h3>
        <p>Express your unique and personalized style with our expert wheel coloring service.</p>
        <a>Request a Quote &nbsp;›</a>
      </div>
    </div>
  </section>

  <section class="section mission">
    <h2 class="abs sec-title" style="top:55px">Mission Statement</h2>
    <p class="abs sec-text" style="top:99px">Our mission is to deliver unparalleled quality and craftsmanship in alloy wheel repair and customization services, enhancing the aesthetic and functional performance of vehicles while ensuring the customer satisfaction through our dedication.</p>
    <div class="abs feature" style="left:87px;top:161px"><svg width="10" height="10" viewBox="0 0 10 10"><circle cx="5" cy="5" r="4.3" fill="none" stroke="#468cc9" stroke-width=".8"/><path d="M3 5l1.5 1.5L7 3.8" stroke="#468cc9" fill="none" stroke-width=".8"/></svg>Precision<br>Restoration</div>
    <div class="abs feature" style="left:87px;top:214px"><svg width="10" height="10" viewBox="0 0 10 10"><circle cx="5" cy="5" r="4.3" fill="none" stroke="#468cc9" stroke-width=".8"/><path d="M3 5l1.5 1.5L7 3.8" stroke="#468cc9" fill="none" stroke-width=".8"/></svg>Customization<br>Expertise</div>
    <div class="abs feature" style="left:605px;top:161px"><svg width="10" height="10" viewBox="0 0 10 10"><circle cx="5" cy="5" r="4.3" fill="none" stroke="#468cc9" stroke-width=".8"/><path d="M3 5l1.5 1.5L7 3.8" stroke="#468cc9" fill="none" stroke-width=".8"/></svg>Costumer<br>Oriented</div>
    <div class="abs feature" style="left:605px;top:214px"><svg width="10" height="10" viewBox="0 0 10 10"><circle cx="5" cy="5" r="4.3" fill="none" stroke="#468cc9" stroke-width=".8"/><path d="M3 5l1.5 1.5L7 3.8" stroke="#468cc9" fill="none" stroke-width=".8"/></svg>Professional<br>Services</div>
    <div class="abs car-art" role="img" aria-label="Photo of a white sports coupe"></div>
    <div class="abs wheels-art" role="img" aria-label="Photo of a stack of tyres with alloy wheels"></div>
  </section>

  <section class="section video" role="img" aria-label="Video still of a dark alloy wheel with drilled brake disc and blue caliper">
    <div class="abs play"></div>
    <svg class="abs" style="left:386px;top:85px" width="12" height="14" viewBox="0 0 12 14"><path d="M1 1l10 6-10 6z" fill="#fff"/></svg>
  </section>

  <section class="section what">
    <h2 class="abs sec-title" style="top:54px">What We Do</h2>
    <p class="abs sec-text" style="top:94px">At Rimhaven Wheelcraft, whether it is restoring, customizing, or replacing wheels, our commitment to excellence and <b style="color:#333;font-weight:500">exceptional customer service guarantees</b> a seamless and satisfying experience for all your wheel needs</p>
    <div class="abs offer" style="left:93px;top:166px">
      <svg width="38" height="38" viewBox="0 0 38 38"><circle cx="19" cy="19" r="17" fill="none" stroke="#1e1e1d" stroke-width="1.3"/><circle cx="19" cy="19" r="12" fill="none" stroke="#468cc9" stroke-width="1.3"/><circle cx="19" cy="19" r="3" fill="#1e1e1d"/><path d="M19 7v9M19 22v9M7 19h9M22 19h9" stroke="#468cc9" stroke-width="2"/></svg>
      <h4>Wheel Refinishing</h4><p>Vestibulum tortor risus, rutrum at congue sed ultricies finibus.</p>
    </div>
    <div class="abs offer" style="left:248px;top:166px">
      <svg width="38" height="38" viewBox="0 0 38 38"><rect x="3" y="6" width="5" height="28" fill="none" stroke="#1e1e1d" stroke-width="1.3"/><circle cx="24" cy="14" r="9" fill="none" stroke="#468cc9" stroke-width="1.3"/><circle cx="24" cy="14" r="3" fill="#1e1e1d"/><path d="M8 28h26v6H8zM8 20h8" fill="none" stroke="#1e1e1d" stroke-width="1.3"/></svg>
      <h4>Wheel Straightening</h4><p>Vestibulum tortor risus, rutrum at congue sed ultricies finibus.</p>
    </div>
    <div class="abs offer" style="left:403px;top:166px">
      <svg width="38" height="38" viewBox="0 0 38 38"><circle cx="16" cy="16" r="11" fill="none" stroke="#1e1e1d" stroke-width="1.3" stroke-dasharray="4 2"/><circle cx="16" cy="16" r="5" fill="none" stroke="#468cc9" stroke-width="1.3"/><circle cx="25" cy="25" r="6" fill="none" stroke="#468cc9" stroke-width="1.3"/><path d="M29 29l6 6" stroke="#1e1e1d" stroke-width="2"/></svg>
      <h4>Wheel Repair</h4><p>Vestibulum tortor risus, rutrum at congue sed ultricies finibus.</p>
    </div>
    <div class="abs offer" style="left:558px;top:160px">
      <svg width="44" height="44" viewBox="0 0 44 44"><circle cx="16" cy="28" r="13" fill="none" stroke="#1e1e1d" stroke-width="1.3"/><circle cx="16" cy="28" r="8" fill="none" stroke="#468cc9" stroke-width="1.5"/><circle cx="16" cy="28" r="2.5" fill="#1e1e1d"/><path d="M28 4h8v6h-8zM32 10v8M26 7h-4" fill="none" stroke="#1e1e1d" stroke-width="1.3"/><path d="M38 14l4 4" stroke="#468cc9" stroke-width="1.3"/></svg>
      <h4 style="margin-top:0">Wheel Coloring</h4><p>Vestibulum tortor risus, rutrum at congue sed ultricies finibus.</p>
    </div>
  </section>

  <section class="section gallery">
    <h2 class="abs gal-title">Shots from<br>Our Gallery</h2>
    <div class="abs circle-btn" style="left:103px;border:1px solid #555"><svg width="12" height="8" viewBox="0 0 12 8"><path d="M11 4H1M4 1L1 4l3 3" stroke="#fff" fill="none"/></svg></div>
    <div class="abs circle-btn" style="left:143px;background:var(--blue)"><svg width="12" height="8" viewBox="0 0 12 8"><path d="M1 4h10M8 1l3 3-3 3" stroke="#fff" fill="none"/></svg></div>
    <div class="abs view-all">View All Gallery &nbsp;&nbsp;›</div>
    <div class="abs shot" style="left:300px;top:59px" role="img" aria-label="Photo of a damaged silver alloy wheel"></div>
    <div class="abs shot" style="left:498px;top:59px" role="img" aria-label="Close-up photo of a silver wheel spoke"></div>
    <div class="abs shot" style="left:696px;top:59px;width:87px" role="img" aria-label="Photo of a wheel with brake caliper"></div>
    <div class="abs shot" style="left:300px;top:201px" role="img" aria-label="Photo of a refinished silver alloy wheel"></div>
    <div class="abs shot" style="left:498px;top:201px" role="img" aria-label="Close-up photo of a polished wheel spoke"></div>
    <div class="abs shot" style="left:696px;top:201px;width:87px" role="img" aria-label="Photo of a multi-spoke alloy wheel"></div>
  </section>

  <section class="section reviews">
    <h2 class="abs sec-title" style="top:55px">Client Reviews</h2>
    <article class="abs card" style="left:101px">
      <div class="card-head"><div class="avatar" role="img" aria-label="Reviewer photo"></div><div class="who">Dale Pruitt<small>14 Hours Ago</small></div><span class="source"></span></div>
      <div class="stars">★★★★★</div>
      <p>Rimhaven Wheelcraft exceeded my expectations with their wheel repair service. My scratched and dented wheels looked brand new after their meticulous work. I couldn't be happier with the results!</p>
    </article>
    <article class="abs card" style="left:299px">
      <div class="card-head"><div class="avatar" role="img" aria-label="Reviewer photo"></div><div class="who">Dale Pruitt<small>14 Hours Ago</small></div><span class="source"></span></div>
      <div class="stars">★★★★★</div>
      <p>I wanted to give my car a fresh look, and Rimhaven Wheelcraft did an amazing job with custom wheel coloring. They helped me choose the perfect finish, and now my car stands out wherever I go. Highly recommended and a place to go!</p>
    </article>
    <article class="abs card" style="left:497px">
      <div class="card-head"><div class="avatar" role="img" aria-label="Reviewer photo"></div><div class="who">Dale Pruitt<small>14 Hours Ago</small></div><span class="source"></span></div>
      <div class="stars">★★★★★</div>
      <p>When I needed a wheel replacement in a hurry, Rimhaven Wheelcraft came to the rescue. Their quick and professional service got me back on the road safely. Many thanks for your expertise and efficiency</p>
    </article>
    <div class="abs dots"><b></b><b></b><b class="on"></b><b></b><b></b></div>
  </section>

  <footer class="section footer">
    <div class="abs brand" style="left:101px;top:64px">RIMHAVEN<small>WHEELCRAFT</small></div>
    <span class="abs social" style="left:101px"></span>
    <span class="abs social" style="left:121px"></span>
    <span class="abs social" style="left:141px"></span>

    <div class="abs f-head" style="left:349px;top:58px">Sitemap</div>
    <div class="abs f-list" style="left:349px;top:76px">About<br>Our Services<br>Project Gallery<br>Clients<br>Contact Us</div>

    <div class="abs f-head" style="left:474px;top:58px">Become a Rimhaven Wheelcraft Insider</div>
    <div class="abs email">Enter Your Email Address</div>
    <div class="abs subscribe">Subscribe Now</div>

    <div class="abs f-head" style="left:349px;top:176px">Working Hours</div>
    <div class="abs f-list" style="left:349px;top:194px;line-height:12px">Mon - Fri<br>09:00 AM - 05:00 PM<br>Sun - CLOSED</div>
    <div class="abs f-head" style="left:474px;top:176px">Contact Info</div>
    <div class="abs f-list" style="left:474px;top:194px;line-height:12px">hello@rimhavenwheel.com<br>555 014 2290</div>
    <div class="abs f-head" style="left:613px;top:176px">Address</div>
    <div class="abs f-list" style="left:613px;top:194px;line-height:12px">42 Orchard Lane,<br>Fairvale PA 10000</div>

    <div class="abs f-rule"></div>
    <div class="abs legal" style="left:101px;color:var(--blue);font-weight:400">© 2023. All rights reserved.</div>
    <div class="abs legal" style="left:474px">PRIVACY POLICY</div>
    <div class="abs legal" style="left:548px">COOKIES POLICY</div>
    <div class="abs legal" style="left:623px">TERMS &amp; CONDITIONS</div>
  </footer>

</main>
</body>
</html>
```